Medical Waste Company with Logo

Need a business card design that targets office managers in the medical community. This card will be the front line for our sales team to market our services to the community. We would like to have email, phone number, website. Please use the logo attached to create a design that we would be proud of.

Target Market(s)

Medical Clients

Industry/Entity Type

Medical Supply

Contact Information for Business Card

Please use logo attached

Colors

Designer to choose colors to be used in the design.

Requirements
Must have
• Our logo (see attached file)
Nice to have
• Maybe a pop of some sort, raised..?

```html
<!DOCTYPE html>
<html lang="en">
<head>
<meta charset="utf-8">
<title>Northpeak Disposal – Business Card</title>
<link rel="stylesheet" href="https://fonts.googleapis.com/css2?family=Montserrat:wght@600;700&family=Lato:wght@400&display=swap">
<style>
  :root {
    --backdrop: #8a5a34;
    --kraft-light: #dcbb8c;
    --kraft-mid: #c89d68;
    --kraft-dark: #b5854f;
    --ink: #111111;
    --shadow: rgba(0, 0, 0, 0.45);
  }
  html, body {
    margin: 0;
    padding: 0;
    width: 1200px;
    height: 900px;
    overflow: hidden;
    background: var(--backdrop);
  }
  .canvas {
    position: relative;
    width: 1200px;
    height: 900px;
  }
  .card {
    position: absolute;
    background: radial-gradient(ellipse at 30% 15%, var(--kraft-light) 0%, var(--kraft-mid) 55%, var(--kraft-dark) 100%);
    box-shadow: 3px 4px 6px var(--shadow);
    color: var(--ink);
    text-align: center;
  }
  .card-contact { left: 330px; top: 90px; width: 555px; height: 343px; }
  .card-brand { left: 330px; top: 470px; width: 558px; height: 342px; }

  .holder-name {
    position: absolute;
    top: 87px; left: 0; right: 0;
    margin: 0;
    font-family: "Montserrat", sans-serif;
    font-weight: 700;
    font-size: 18px;
    letter-spacing: 0.4px;
  }
  .holder-title {
    position: absolute;
    top: 110px; left: 0; right: 0;
    margin: 0;
    font-family: "Lato", sans-serif;
    font-size: 15px;
  }
  .contact-divider {
    position: absolute;
    top: 174px;
    left: 183px;
    width: 188px;
    height: 18px;
  }
  .contact-list {
    position: absolute;
    top: 195px; left: 0; right: 0;
    margin: 0; padding: 0;
    list-style: none;
    font-family: "Lato", sans-serif;
    font-size: 15px;
    line-height: 20px;
  }

  .brand-dot {
    position: absolute;
    top: 86px;
    left: 229px;
    width: 100px;
    height: 100px;
    border-radius: 50%;
    background: var(--ink);
  }
  .brand-name {
    position: absolute;
    top: 199px; left: 0; right: 0;
    margin: 0;
    font-family: "Montserrat", sans-serif;
    font-weight: 700;
    font-size: 29px;
    letter-spacing: 0.5px;
    color: var(--ink);
  }
</style>
</head>
<body>
<main class="canvas">

  <section class="card card-contact" aria-label="Card with contact details">
    <h1 class="holder-name">DANIEL HARTLEY</h1>
    <p class="holder-title">Managing Director</p>

    <svg class="contact-divider" viewBox="0 0 188 18" aria-hidden="true">
      <line x1="0" y1="9" x2="62" y2="9" stroke="#111" stroke-width="1"/>
      <line x1="126" y1="9" x2="188" y2="9" stroke="#111" stroke-width="1"/>
      <circle cx="72" cy="9" r="8.5" fill="#111"/>
      <path d="M68.8 5.2c.5-.4 1.1-.3 1.4.2l.8 1.4c.2.4.1.9-.3 1.2l-.5.4c.5 1.2 1.4 2.1 2.6 2.6l.4-.5c.3-.4.8-.5 1.2-.3l1.4.8c.5.3.6.9.2 1.4-.8 1-2 1.3-3.1.8-2-1-3.6-2.6-4.6-4.6-.5-1.1-.2-2.3.5-3.4z" fill="#d2ac7a"/>
      <circle cx="94" cy="9" r="8.5" fill="#111"/>
      <rect x="89.5" y="5.8" width="9" height="6.4" fill="#d2ac7a"/>
      <path d="M89.5 5.8 94 9.6 98.5 5.8" fill="none" stroke="#111" stroke-width="1"/>
      <circle cx="116" cy="9" r="8.5" fill="#111"/>
      <circle cx="116" cy="9" r="4.6" fill="none" stroke="#d2ac7a" stroke-width="1.2"/>
      <ellipse cx="116" cy="9" rx="2" ry="4.6" fill="none" stroke="#d2ac7a" stroke-width="1"/>
      <line x1="111.4" y1="9" x2="120.6" y2="9" stroke="#d2ac7a" stroke-width="1"/>
    </svg>

    <ul class="contact-list">
      <li>444 555 0192</li>
      <li>info@northpeak.com</li>
      <li>www.northpeakco.com</li>
    </ul>
  </section>

  <section class="card card-brand" aria-label="Card with company name">
    <span class="brand-dot" aria-hidden="true"></span>
    <p class="brand-name">NORTHPEAK DISPOSAL</p>
  </section>

</main>
</body>
</html>
```